依頼詳細
プロが業務用の高圧洗浄機を使い、ご自宅の外構・駐車場(ガレージ)・ブロック塀・玄関タイル・を綺麗にされたい方を募集します。
泥、排気ガスの汚れ、コケ、ほこり等を綺麗に致します。
お見積りは無料
高圧洗浄専門店
割引制度有
平日割引あり(火曜日・水曜日は特別料金にて実施)(空き状況はお電話にてご確認下さい)
施工料金等、丁寧に分かりやすくご説明します。
作業時間平均:2時間~3時間
料金:33,000円~
作業時:水道をお借りします
まずは、お気軽にご相談下さい。
株式会社ミドリノハウジング
TEL:094ー318-5562
担当:坂巻(さかまき)・梅沢(うめざわ)
営業時間:9:00~19:00

記載項目
株式会社ミドリノハウジング
094-318-5562
料金:33,000円~(範囲によって異なります)
プロの高圧洗浄はミドリノハウジングにお任せください。
サイズ
A4
ページ数
片面
希望イメージ
シンプル 複雑
単色 カラフル
暗い 明るい
日常 高級
遊び心 厳粛
未来的 伝統的
女性的 男性的
希望する色
水色系、ターコイズブルーの使用をお願い致します。
納品ファイル
• 高解像度JPG (.jpg)
補足説明
会社ロゴを添付しておりますので、ロゴの使用をお願い致します。
■ 選んだ理由

見やすく、弊社希望のチラシに近いものでした。
頂きました案件全てのチラシ案を印刷し、三つ折りにしましたが、一番良かったです。
伝えたい内容も、しっかり入っており、戸建てとなると年配の方が多いと思われ、その点でも大事な部分は文字が大きく見やすさも良く選ばせて頂きました。

■ 提案者全員のお礼・コメント

初めての依頼となりましたが、多数の応募を頂きましてありがとうございました。
正直、こんなに多数の応募を頂けるとは思ってませんでしたので驚きました。
今後もチラシの案をご依頼する事もるかと思いますので、宜しくお願い致します。

```html
<!DOCTYPE html>
<html lang="ja">
<head>
<meta charset="utf-8">
<title>高圧洗浄 外構洗浄チラシ</title>
<link href="https://fonts.googleapis.com/css2?family=Noto+Sans+JP:wght@400;500;700;900&display=swap" rel="stylesheet">
<style>
:root{
  --cyan:#19a9dc;
  --blue:#1f78c8;
  --navy:#1b3d78;
  --red:#e2262c;
  --yellow:#ffe44d;
  --ink:#2a2a2a;
  --paper:#ffffff;
  --pale:#e8f6fc;
}
*{margin:0;padding:0;box-sizing:border-box}
html,body{width:851px;height:1200px;overflow:hidden;background:var(--paper)}
body{font-family:"Noto Sans JP",sans-serif;color:var(--ink)}
.flyer{position:relative;width:851px;height:1200px;overflow:hidden;background:var(--paper)}

.photo{position:absolute}
.photo-exterior{left:0;top:0;width:400px;height:275px;background:linear-gradient(160deg,#cfe3f2 0%,#e9eef2 45%,#9aa6ae 100%)}
.photo-garage{left:404px;top:0;width:447px;height:275px;background:linear-gradient(200deg,#8fc3e6 0%,#b9c4cc 50%,#6f7a82 100%)}
.photo-block{left:0;top:279px;width:400px;height:316px;background:linear-gradient(180deg,#8a8a82 0%,#a9a79c 50%,#6e6d66 100%)}
.photo-tile{left:404px;top:279px;width:447px;height:316px;background:linear-gradient(170deg,#e6e8ea 0%,#cfd3d6 60%,#b0b5b9 100%)}
.photo-shade{position:absolute;left:0;top:0;width:851px;height:595px;background:linear-gradient(180deg,rgba(10,40,80,.15),rgba(10,40,80,.35) 60%,rgba(10,40,80,.1))}

.tag{position:absolute;background:rgba(255,255,255,.92);color:var(--navy);font-weight:700;font-size:17px;padding:3px 12px}
.tag-exterior{left:8px;top:244px}
.tag-garage{right:8px;top:244px}
.tag-block{left:8px;top:562px}
.tag-tile{right:8px;top:562px}

.headline{position:absolute;left:0;top:48px;width:851px;text-align:center;color:#fff;font-weight:900}
.headline .line{display:block;text-shadow:0 2px 6px rgba(0,30,70,.55)}
.line-pro{display:inline-block!important;background:var(--blue);font-size:50px;padding:0 22px;line-height:72px;text-shadow:none!important}
.line-machine{font-size:60px;line-height:86px}
.line-focus{display:inline-block!important;background:var(--blue);font-size:92px;line-height:118px;padding:0 26px;margin-top:6px;text-shadow:none!important}
.line-ask{font-size:88px;line-height:118px}

.badge{position:absolute;left:250px;top:500px;width:351px;height:56px;border-radius:28px;background:var(--yellow);color:var(--red);font-weight:900;font-size:26px;text-align:center;line-height:56px;box-shadow:0 3px 0 rgba(0,0,0,.2)}

.special{position:absolute;left:28px;top:606px;display:flex;align-items:center;gap:6px;font-weight:900;font-size:40px;color:var(--red);white-space:nowrap}
.special .box{background:var(--red);color:#fff;padding:0 10px;line-height:54px}

.notes{position:absolute;left:36px;top:664px;width:780px;display:flex;justify-content:space-between;font-size:15px;color:#555}

.pro-band{position:absolute;left:28px;top:706px;width:560px;height:46px;background:var(--pale);border-left:8px solid var(--cyan);color:var(--blue);font-weight:900;font-size:30px;line-height:46px;padding-left:16px}
.washer{position:absolute;left:610px;top:692px;width:210px;height:170px;border-radius:10px;background:linear-gradient(135deg,#bfe6f6,#4db7e2)}

.intro{position:absolute;left:36px;top:770px;width:560px;font-size:17px;line-height:1.75;color:#333;font-weight:500}

.facts{position:absolute;left:36px;top:890px;list-style:none;font-size:19px;line-height:1.9;font-weight:500}
.facts li::before{content:"";display:inline-block;width:10px;height:10px;background:var(--cyan);margin-right:10px;vertical-align:2px}

.divider{position:absolute;left:28px;top:1000px;width:795px;height:3px;background:var(--cyan)}

.price{position:absolute;left:28px;top:1060px;display:flex;align-items:flex-end;gap:14px;white-space:nowrap}
.price-label{background:var(--cyan);color:#fff;font-weight:900;font-size:26px;width:64px;padding:8px 0;text-align:center;line-height:1.2}
.price-value{color:var(--red);font-weight:900;font-size:96px;line-height:1;letter-spacing:-2px}
.price-unit{color:var(--red);font-weight:900;font-size:36px;line-height:1.6}
.price-note{position:absolute;left:28px;top:1176px;font-size:12px;color:#666;white-space:nowrap}

.estimate{position:absolute;left:478px;top:1022px;width:80px;height:80px;border-radius:50%;background:var(--red);color:#fff;font-weight:900;font-size:20px;line-height:1.2;display:flex;align-items:center;justify-content:center;text-align:center}
.consult{position:absolute;left:574px;top:1024px;font-size:16px;font-weight:700;color:var(--navy);white-space:nowrap}
.company{position:absolute;left:574px;top:1058px;display:flex;align-items:center;gap:8px;white-space:nowrap}
.company-mark{width:24px;height:24px;background:var(--blue)}
.company-name{font-weight:700;font-size:17px;color:var(--navy)}
.phone{position:absolute;left:568px;top:1096px;display:flex;align-items:center;gap:6px;color:var(--blue);font-weight:900;font-size:32px;line-height:1;letter-spacing:-.5px;white-space:nowrap}
.footer{position:absolute;right:20px;top:1150px;font-size:12px;color:#444;display:flex;gap:14px;white-space:nowrap}
</style>
</head>
<body>
<main class="flyer">
  <div class="photo photo-exterior" role="img" aria-label="洗浄後の戸建て住宅の外構の写真"></div>
  <div class="photo photo-garage" role="img" aria-label="住宅のガレージと駐車場の写真"></div>
  <div class="photo photo-block" role="img" aria-label="石積みのブロック塀の写真"></div>
  <div class="photo photo-tile" role="img" aria-label="洗浄された玄関タイルの写真"></div>
  <div class="photo-shade"></div>

  <span class="tag tag-exterior">外構</span>
  <span class="tag tag-garage">ガレージ</span>
  <span class="tag tag-block">ブロック塀</span>
  <span class="tag tag-tile">玄関タイル</span>

  <h1 class="headline">
    <span class="line line-pro">プロによる業務用</span>
    <span class="line line-machine">高圧洗浄機で</span>
    <span class="line line-focus">外構洗浄</span>
    <span class="line line-ask">しませんか</span>
  </h1>

  <p class="badge">お得な平日格安プラン実施中!</p>

  <p class="special"><span class="box">火曜日</span><span class="box">水曜日</span>は<span class="box">特別料金</span>にて実施中!!</p>

  <div class="notes">
    <span>※空き状況はお電話にてご確認下さい</span>
    <span>※施工料金等、丁寧に分かりやすくご説明します。</span>
  </div>

  <h2 class="pro-band">高圧洗浄のプロにお任せください。</h2>
  <div class="washer" role="img" aria-label="業務用高圧洗浄機のイラスト"></div>

  <p class="intro">ご自宅の外構・駐車場(ガレージ)・ブロック塀・玄関タイルなどを、プロが業務用の高圧洗浄機を使い綺麗にいたします。泥、排気ガスの汚れ、コケ、ほこり等もすっきり落とします。</p>

  <ul class="facts">
    <li>作業時間平均:2時間〜3時間程度</li>
    <li>作業時、水道をお借りします。</li>
  </ul>

  <div class="divider"></div>

  <div class="price">
    <span class="price-label">料<br>金</span>
    <span class="price-value">33,000</span>
    <span class="price-unit">円〜</span>
  </div>
  <p class="price-note">※範囲によって異なります</p>

  <div class="estimate">見積<br>無料</div>
  <p class="consult">まずは、お気軽にご相談下さい。</p>
  <div class="company">
    <span class="company-mark"></span>
    <span class="company-name">株式会社ミドリノハウジング</span>
  </div>
  <p class="phone">
    <svg width="28" height="28" viewBox="0 0 24 24" aria-hidden="true"><path fill="currentColor" d="M6.6 10.8a15.1 15.1 0 0 0 6.6 6.6l2.2-2.2a1 1 0 0 1 1-.25 11.4 11.4 0 0 0 3.6.57 1 1 0 0 1 1 1V20a1 1 0 0 1-1 1A17 17 0 0 1 3 4a1 1 0 0 1 1-1h3.5a1 1 0 0 1 1 1c0 1.25.2 2.45.57 3.6a1 1 0 0 1-.25 1z"/></svg>
    094-318-5562
  </p>
  <div class="footer">
    <span>営業時間:9:00〜19:00</span>
    <span>担当:坂巻(さかまき)・梅沢(うめざわ)</span>
  </div>
</main>
</body>
</html>
```